Web 2.0 my 1 page website ($500 Guaranteed)

Im looking for someone who can update my existing design at http://www.doriselvanby.com
I like existing layout and the way the boxes all work. Looking for the same design but with an updated web 2.0 textured look and feel.
Please note the current site is already working on top of pagecrate and new design needs to also work with pagecrate so I can continue to page content.
Looking for designer who can also get it working in pagecrate as it is today.
$500 AUD first prize for it all working.
If it helps:
I like minimailist. I like white. I like bright. I like texture. I like backgrounds. I like horizontal stripes running the length of the page. I like designs that work regardless of width of page. I like big bold statements. I like obvious. I like round edges. I like sites that look like they have come alive. I like depth. I like a 3D look. I like something very subtle that moves occassionally - just enough to catch your eye. I dont like popups. I dont like scrolling.
I like really clean SEO friendly source code. I like standards compatible design.
http://www.lotvessel.ie/ I like the depth of the mini coming out of the screen. I like the big bold fonts and the bright colours. I like the horizontal red stripe running the length of the page.
http://www.quillharbor.ie/ I like the backround clouds. I like the nice big lettering on the font on the mene bar. I like the nice bog boxes and contact numbers.
http://www.kuljepolkuja.fi/ I like the bright colours on the phone. I like the splash of the bubbles at the top of the page.
http://ontheruncue.me/ I like the blurred background. I REALLY like the rounded enter your email and notify me text boxes. I like the fonts on notify me and the textured background of the button.
http://9qtorn.com/it/ I really like the horizontal bar across the page - I like the big fonts in this background - I like the green and the orange. I really like the depth - how the beans and chair and butterfly sit on top of the page kind of bringing it to life. Like all the layers giving that illusion of 3D.
http://www.fenwrigley.net/ Like the big fonts, the horizontal bar, the leather stitching look around the "lets work together" and how everything is shadowed and sits off the page. I like the big contact us / get in touch / fonts at the bottom the big social media buttons. Probably this area could all be half the size but I like it.
http://www.drevoxis.com/ I like the graining textures in the background grays. I prefer blues and whites.
http://tibbinshedding.ca/ Like the big bold texts and the colours. Like the 3D cardboard box coming off the page.
http://pondchimers.com/ Like the textured backround - the rough grainy blue.
http://www.uk-rv.com/ I always liked those background kind of bursts behind the bay area picture in the middle. Like the striped blue background.
http://workshop.vendoqua.com/ Who doesnt like a ninja, but again like the big fonts and the way the person has depth
http://www.plumfolders.com/ I like the depth. I like the big bold colours.
http://www.5ibrelt.com/ Again like how the product is featured with lighting behind it, has that 3D look. Nice big lettering etc.
Updates
I like minimailist. I like white. I like bright. I like texture. I like
backgrounds. I like horizontal stripes running the length of the page. I
like designs that work regardless of width of page. I like big bold
statements. I like obvious. I like round edges. I like sites that look
like they have come alive. I like depth. I like a 3D look. I like
something very subtle that moves occassionally - just enough to catch
your eye. I dont like popups. I dont like scrolling.
http://www.lotvessel.ie/
I like the depth of the mini coming out of the screen. I like the big
bold fonts and the bright colours. I like the horizontal red stripe
running the length of the page.
http://www.quillharbor.ie/
I like the backround clouds. I like the nice big lettering on the font
on the mene bar. I like the nice bog boxes and contact numbers.
http://ontheruncue.me/
I like the blurred background. I REALLY like the rounded enter your
email and notify me text boxes. I like the fonts on notify me and the
textured background of the button.
http://9qtorn.com/it/
I really like the horizontal bar across the page - I like the big fonts
in this background - I like the green and the orange. I really like the
depth - how the beans and chair and butterfly sit on top of the page
kind of bringing it to life. Like all the layers giving that illusion of
3D.
http://www.fenwrigley.net/
Like the big fonts, the horizontal bar, the leather stitching look
around the "lets work together" and how everything is shadowed and sits
off the page. I like the big contact us / get in touch / fonts at the
bottom the big social media buttons. Probably this area could all be
half the size but I like it.
Typical Components of Web 2.0 Site Design
- Lots of space: Web 2.0 sites tend to have a lot of wide-open space. It's a contrast from the 90s, where the trend was to make usage of every square inch of a website's home page with links, banners and applets. White space is embraced to a major degree, as it calls attention to important buttons and links.
- The "Less Is More" Mentality: By putting less on the page, you're drawing more attention to the elements that matter: content and call-to-action buttons. "Clutter" and Web 2.0 simply do not mix - this is a new era of design psychology.
- Gradients: Merely a design element, gradients are used in Web 2.0 site design to give a clean, soft impression that's easy on the eyes.
- Large Fonts: Huge headings are a popular trend in Web 2.0 design - headings are usually taglines that describe or summarize what a website is about in just a handful of words. It's a huge benefit to first-timer usability, especially since new visitors would like to "get to the point" without having to read an intro paragraph.
- Dramatic Color Contrast: Another typical element seen in Web 2.0 design are bright colors (particularly neon colors) that accent site elements including menus, separator bars and footers. Many sites use this same neon color for their hyperlinks and headings, as well. Sometimes, the contrast between bright neon colors and charcoal or light gray text are put in unison for a dramatic effect.
- Eye Candy Logos: In Web 2.0 logo design, it's almost expected to see logos have a shiny plastic luster, or a soft gradient. Most Web 2.0 fonts are similar to basic Arial, Tahoma or Helvetica, and are simple. The colors used within the logo are also typically mimicked on other site design pieces to create a sense of uniformity.
- Huge Buttons: Calls to action (buttons that prompt you to "Get More Information," "Download Now," "See A Demo" or "Buy Now") are typically gigantic in Web 2.0 design. They're also attractive, featuring a color that strays away from the rest of the website's schematic. These buttons are typically isolated by a great deal of space, making them very easy to notice.
- Reflections: Product images, screenshots and icons can be seen as having "reflections" underneath them, as if they were standing on top of a new laminate floor. It's a stereotypical design element of Web 2.0.
- Lots of Icons: Web 2.0 icons are always in vector format, which is the standard format created by software such as Adobe Illustrator and Flash. They're attractive and clean looking, and are used to either draw attention to a website's sub-categories, a product's individual features, or anything else that the web designer wanted to help associate for a viewer.
- Exaggerated Web Form Fields: Huge form fields add to usability and draw attention to sign-ups and registrations. Instead of typing in a search, a username or anything else into a tiny web field, Web 2.0 has evolved them into massive interactive boxes with large text that makes things easy to see. For a good example, look at Glimvo.com's huge fields.

```html
<!DOCTYPE html>
<html lang="en">
<head>
<meta charset="utf-8">
<title>Doris Elvanby</title>
<link rel="stylesheet" href="https://fonts.googleapis.com/css2?family=Jura:wght@400;500&family=Noto+Serif:ital@1&display=swap">
<style>
:root{
  --orange:#e8781e;
  --orange-deep:#d9620a;
  --orange-light:#f7a24a;
  --ink:#222;
  --ink-soft:#3a2410;
  --white:#fff;
  --nav:#151515;
  --grey:#888;
}
*{margin:0;padding:0;box-sizing:border-box}
html,body{width:1200px;height:922px;overflow:hidden;background:var(--white)}
body{position:relative;font-family:"Noto Serif",Georgia,serif;font-style:italic;color:var(--ink)}
.display{font-family:"Jura",sans-serif;font-style:normal;font-weight:400}

.site-name{position:absolute;left:40px;top:30px;font-size:58px;letter-spacing:1px;white-space:nowrap}
.site-name .first{color:var(--orange)}
.site-name .last{color:#111;margin-left:22px}

.find-me{position:absolute;right:0;top:56px;width:166px;height:50px;border-radius:10px 0 0 10px;
  background:linear-gradient(#f39232,var(--orange-deep));color:var(--white);font-size:23px;
  padding:9px 0 0 26px;box-shadow:0 2px 4px rgba(0,0,0,.25)}
.find-me::after{content:"";position:absolute;left:56px;bottom:-13px;border:9px solid transparent;border-top:13px solid var(--orange-deep);border-bottom:0}
.social{position:absolute;right:0;top:118px;width:188px;height:60px;background:var(--white);
  border-radius:10px 0 0 10px;box-shadow:0 2px 6px rgba(0,0,0,.3);z-index:3;
  display:flex;justify-content:space-around;align-items:center;padding:0 6px;list-style:none}
.social li{display:flex;flex-direction:column;align-items:center;gap:3px;font-size:11px;color:#1a5fa8;font-style:normal}
.social .mark{width:24px;height:24px;border-radius:4px;background:#1a5fa8}

.hero{position:absolute;left:0;top:133px;width:1200px;height:408px;
  background:radial-gradient(ellipse at 55% 45%,#f9a13a 0%,#ef8420 45%,#d9620a 100%)}
.portrait{position:absolute;left:40px;top:22px;width:390px;height:386px;
  background:linear-gradient(180deg,#7a4a2a 0%,#2b2220 35%,#171717 75%,rgba(23,23,23,0) 100%);
  border-radius:120px 120px 0 0}
.hero-title{position:absolute;left:466px;top:63px;color:var(--white);font-size:60px;letter-spacing:1px}
.hero-text{position:absolute;left:466px;top:148px;width:720px;font-size:25px;line-height:35px;color:var(--ink-soft)}
.slides{position:absolute;left:1050px;top:320px;display:flex;gap:8px}
.slides span{width:14px;height:14px;border-radius:50%;background:var(--white)}
.slides span.off{background:#b8500a}

.main-nav{position:absolute;left:625px;top:500px;width:550px;height:68px;border-radius:10px 10px 14px 14px;
  background:linear-gradient(#1c1c1c 0%,#0c0c0c 55%,#3a3a3a 80%,#222 100%);box-shadow:0 4px 8px rgba(0,0,0,.35);z-index:2}
.main-nav ul{list-style:none;display:flex;justify-content:space-around;padding:17px 14px 0}
.main-nav a{color:var(--white);text-decoration:none;font-size:18px}
.main-nav a.current{color:var(--orange)}

.section-title{position:absolute;color:var(--orange);font-size:40px;letter-spacing:2px}
.welcome-title{left:46px;top:585px}
.projects-title{left:745px;top:580px}
.welcome-text{position:absolute;left:50px;top:648px;width:625px;font-size:14.2px;line-height:21.5px}
.welcome-text p+p{margin-top:8px}
.project-image{position:absolute;left:742px;top:635px;width:410px;height:111px;border:1px solid #222;
  background:linear-gradient(90deg,#6b5a44,#b9a88c 30%,#8e7c62 55%,#c7c1b5 80%,#5e6a74)}
.project-text{position:absolute;left:745px;top:766px;width:430px;font-size:14.2px;line-height:21.5px}
.more{position:absolute;top:831px;display:flex;align-items:center;gap:6px;color:var(--grey);font-size:14px;text-decoration:none}
.more .pill{width:26px;height:12px;border-radius:6px;background:linear-gradient(#f3f3f3,#bdbdbd);border:1px solid #aaa}
.more.accent .pill{background:linear-gradient(#ffb060,var(--orange-deep));border-color:#c65a08}
.more-welcome{left:590px}
.more-projects{left:1082px}

.site-footer{position:absolute;left:28px;top:879px;width:1144px;border-top:1px solid var(--orange)}
.copyright{position:absolute;right:40px;top:892px;font-size:12px;color:#222}
</style>
</head>
<body>
<header>
  <h1 class="site-name display"><span class="first">Doris</span><span class="last">Elvanby</span></h1>
  <div class="find-me">Find me on</div>
  <ul class="social">
    <li><span class="mark"></span>Facelot</li>
    <li><span class="mark"></span>Chirpwell</li>
    <li><span class="mark"></span>Linkvale</li>
  </ul>
</header>

<section class="hero">
  <div class="portrait" role="img" aria-label="Portrait photo of the site owner, smiling, in a dark shirt"></div>
  <h2 class="hero-title display">My Self</h2>
  <p class="hero-text">Retai CIO with Passion for multi-Channel, Multi-Store technology. Specialise in using Online Communities to help drive the business by consumer engagement.</p>
  <div class="slides"><span></span><span></span><span></span><span class="off"></span></div>
</section>

<nav class="main-nav">
  <ul>
    <li><a class="current" href="#">Home</a></li>
    <li><a href="#">Profile</a></li>
    <li><a href="#">Career</a></li>
    <li><a href="#">My Interests</a></li>
    <li><a href="#">Contact</a></li>
  </ul>
</nav>

<main>
  <h2 class="section-title welcome-title display">Welcome</h2>
  <div class="welcome-text">
    <p>Hello, and welcome to my home page on the web. There isn't really much going on here, more just a front end for my webmail etc. For those that are interested in learning a bit more about me personally or commercially, feel free to click around and have a look.</p>
    <p>My background is basically a sales guy who a long time ago learnt how to use technology to reach the masses. After running BBS's for years to support our computer business, I built my first commercial web site around 1994 and quickly moved into full blown eCommerce sites. Did a stint next in Web Marketing and SEO which lead to a couple of years of hammering affiliate programs and Searchly Adverts across the web.</p>
  </div>
  <a class="more more-welcome" href="#"><span class="pill"></span>More...</a>

  <h2 class="section-title projects-title display">Our Latest Projects</h2>
  <div class="project-image" role="img" aria-label="Photo of a retail showroom with staff and display screens"></div>
  <p class="project-text">There are many variations of passages of Lorem Ipsum available, but the majority have suffered alteration in some form, by injected humour, or randomised words .</p>
  <a class="more more-projects accent" href="#"><span class="pill"></span>More...</a>
</main>

<footer>
  <div class="site-footer"></div>
  <p class="copyright">Copyright © 2011.www.doriselvanby.com</p>
</footer>
</body>
</html>
```